ALL TEXT Social Media Graphics

We are looking for a series of social media graphics for Instagram (new size: 4:5 (1080 x 1350 pixels) ratio that are ALL TEXT. We want the following quotes below on each graphic; one quote per graphic. AND, In very small letters at the bottom of each graphic, add @PaulaWrenLive
The look and feel of these graphics should be complimentary to the color palette attached below; but keep them simple. But the design is up to you; at the end of this document, I provided various samples of all text graphics that I like as examples.
The Quotes are in the attached WORD document
women trying to lose weight

```html
<!DOCTYPE html>
<html lang="en">
<head>
<meta charset="utf-8">
<title>All Text Social Graphics – Summer Slimdown Series</title>
<link href="https://fonts.googleapis.com/css2?family=League+Gothic&family=Montserrat:ital,wght@1,700&display=swap" rel="stylesheet">
<style>
  :root {
    --backdrop: #808080;
    --paper: #ffffff;
    --magenta: #b0185a;
    --pink: #f08db4;
    --ink: #111111;
    --charcoal: #333333;
    --handle-grey: #8a8a8a;
  }
  html, body {
    margin: 0;
    padding: 0;
    width: 1200px;
    height: 578px;
    overflow: hidden;
    background: var(--backdrop);
  }
  .board {
    position: relative;
    width: 1200px;
    height: 578px;
  }
  .card {
    position: absolute;
    width: 194px;
    height: 245px;
    background: var(--paper);
  }
  .frame {
    position: absolute;
    inset: 6px;
    border: 3px solid var(--magenta);
  }
  .content {
    position: absolute;
    left: 4px;
    right: 4px;
    top: 14px;
    bottom: 24px;
    display: flex;
    flex-direction: column;
    align-items: center;
    justify-content: center;
    text-align: center;
    font-family: "League Gothic", "Oswald", sans-serif;
    line-height: 1;
  }
  .content > div { white-space: nowrap; }
  .handle {
    position: absolute;
    left: 0;
    right: 0;
    bottom: 14px;
    text-align: center;
    font-family: "Montserrat", sans-serif;
    font-style: italic;
    font-weight: 700;
    font-size: 8px;
    color: var(--handle-grey);
  }
  .kicker { color: var(--pink); font-size: 18px; }
  .kicker-lg { color: var(--pink); font-size: 32px; }
  .head { color: var(--ink); font-size: 42px; }
  .head-md { color: var(--ink); font-size: 25px; }
  .head-dark { color: var(--charcoal); font-size: 40px; }
  .accent { color: var(--magenta); font-size: 27px; }
  .accent-lg { color: var(--magenta); font-size: 40px; }
  .body { color: var(--ink); font-size: 21px; line-height: 1.28; }
  .body b { color: var(--magenta); font-weight: 400; }
  .comment { color: var(--magenta); font-size: 22px; margin-top: 6px; }
  .cta { color: var(--pink); font-size: 15px; margin-top: 4px; }
  .gap { height: 6px; }
</style>
</head>
<body>
<main class="board">

  <!-- Row one -->
  <section class="card" style="left:30px;top:27px">
    <div class="frame"></div>
    <div class="content">
      <div class="kicker" style="font-size:19px">YOU CAN ABSOLUTELY BE DOWN</div>
      <div class="head-dark" style="font-size:37px">20–30 POUNDS</div>
      <div class="accent" style="font-size:28px">BY END OF SUMMER.</div>
      <div class="body">All it takes is the right<br>plan—and you've found it.</div>
      <div class="comment" style="font-size:23px">Comment “Bright”</div>
      <div class="cta" style="font-size:16px">FOR THE BRIGHT SUMMER SLIMDOWN!</div>
    </div>
    <div class="handle">@PaulaWrenLive</div>
  </section>

  <section class="card" style="left:264px;top:27px">
    <div class="frame"></div>
    <div class="content">
      <div class="kicker">YOU DON'T NEED ANOTHER DIET</div>
      <div class="head-md" style="color:var(--charcoal);font-size:28px">YOU NEED A SYSTEM</div>
      <div class="accent-lg" style="font-size:41px">THAT WORKS.</div>
      <div class="body">Drop <b>30 pounds</b> with the<br>Bright Summer Slimdown.</div>
      <div class="comment">Comment “Summer”</div>
      <div class="cta">TO START NOW</div>
    </div>
    <div class="handle">@PaulaWrenLive</div>
  </section>

  <section class="card" style="left:498px;top:27px">
    <div class="frame"></div>
    <div class="content">
      <div class="kicker" style="font-size:23px">THIS SUMMER AIN'T OVER</div>
      <div class="head-dark" style="font-size:42px">AND NEITHER</div>
      <div class="accent" style="font-size:23px">ARE YOUR BODY GOALS.</div>
      <div class="body">Drop <b>30 pounds</b> with the<br>Bright Summer Slimdown.</div>
      <div class="comment">Comment “Bright”</div>
      <div class="cta">TO GET THE PLAN</div>
    </div>
    <div class="handle">@PaulaWrenLive</div>
  </section>

  <section class="card" style="left:731px;top:27px">
    <div class="frame"></div>
    <div class="content">
      <div class="kicker">IF YOUR GOAL IS A TINY WAIST,</div>
      <div class="head" style="font-size:48px">FLAT BELLY,</div>
      <div class="accent" style="font-size:23px">AND 30 POUNDS DOWN</div>
      <div class="body" style="margin-top:6px">this is the plan.</div>
      <div class="comment" style="margin-top:4px">Comment “Summer”</div>
      <div class="gap"></div>
      <div class="cta" style="font-size:14.5px">TO JOIN THE BRIGHT SUMMER SLIMDOWN!</div>
    </div>
    <div class="handle">@PaulaWrenLive</div>
  </section>

  <section class="card" style="left:965px;top:27px">
    <div class="frame"></div>
    <div class="content" style="justify-content:flex-start;padding-top:10px">
      <div class="kicker" style="font-size:17px">THERE'S STILL TIME TO DROP THE</div>
      <div class="head" style="font-size:50px">30 POUNDS</div>
      <div class="accent" style="font-size:23px">AND SLAY THIS SUMMER.</div>
      <div class="body" style="font-size:20px;margin-top:4px">The Bright Summer<br>Slimdown has the blueprint.</div>
      <div class="comment">Comment “Bright”</div>
    </div>
    <div class="handle">@PaulaWrenLive</div>
  </section>

  <!-- Row two -->
  <section class="card" style="left:30px;top:306px">
    <div class="frame"></div>
    <div class="content">
      <div class="kicker-lg">SNATCHED WAIST,</div>
      <div class="head" style="font-size:42px">FLAT TUMMY,</div>
      <div class="accent" style="font-size:28px">30 POUNDS LIGHTER</div>
      <div class="body" style="font-size:18px">that's what the Bright Summer<br>Slimdown Challenge delivers.</div>
      <div class="comment" style="margin-top:2px;font-size:23px">Comment “Bright”</div>
      <div class="cta" style="font-size:14px">TO GET THE PLAN</div>
    </div>
    <div class="handle">@PaulaWrenLive</div>
  </section>

  <section class="card" style="left:264px;top:306px">
    <div class="frame"></div>
    <div class="content">
      <div class="kicker" style="font-size:23.5px">NOTHING FEELS BETTER</div>
      <div class="head-md" style="font-size:22px">THAN SEEING THAT SCALE</div>
      <div class="accent" style="font-size:23px">DROP WEEK AFTER WEEK.</div>
      <div class="body" style="font-size:18px;line-height:1.55;margin-top:6px">Let's lose up to <b>30 pounds</b><br>this summer—together.</div>
      <div class="comment" style="font-size:20.5px">Comment “Summer”</div>
      <div class="cta" style="font-size:14.5px;line-height:0.95">TO JOIN THE BRIGHT<br>SUMMER SLIMDOWN!</div>
    </div>
    <div class="handle">@PaulaWrenLive</div>
  </section>

  <section class="card" style="left:498px;top:306px">
    <div class="frame"></div>
    <div class="content" style="justify-content:flex-start;padding-top:12px">
      <div class="kicker" style="font-size:16.5px">SIS, WE'RE DROPPING BELLY FLAT</div>
      <div class="head-md" style="font-size:25.5px">AND SAYING GOODBYE</div>
      <div class="accent" style="font-size:24.5px">TO STUBBORN POUNDS.</div>
      <div class="body" style="font-size:17.5px;line-height:1.5;margin-top:8px">Join the Bright Summer<br>Slimdown</div>
      <div class="comment" style="font-size:20.5px;margin-top:12px">Comment “Summer”!</div>
    </div>
    <div class="handle">@PaulaWrenLive</div>
  </section>

  <section class="card" style="left:731px;top:306px">
    <div class="frame"></div>
    <div class="content">
      <div class="kicker-lg" style="font-size:48px">DON'T WAIT</div>
      <div class="head-md" style="font-size:29px">'TIL NEXT SUMMER</div>
      <div class="accent-lg" style="font-size:40px">TO GET RIGHT.</div>
      <div class="body" style="font-size:17.5px;line-height:1.2">The time is NOW.<br>Drop <b>30 pounds</b> with the<br>Bright Summer Slimdown.</div>
      <div class="comment" style="margin-top:2px;font-size:20.5px">Comment “Summer”!</div>
    </div>
    <div class="handle">@PaulaWrenLive</div>
  </section>

  <section class="card" style="left:965px;top:306px">
    <div class="frame"></div>
    <div class="content">
      <div class="kicker-lg" style="font-size:28px">YOU'VE GOT 8 WEEKS</div>
      <div class="head-md" style="font-size:24px">AND THE PERFECT PLAN</div>
      <div class="accent" style="font-size:27.5px">TO DROP 30 POUNDS.</div>
      <div class="body" style="font-size:17.5px;line-height:1.25;margin-top:6px">Let's get snatched this<br>summer with the<br>Bright Summer Slimdown.</div>
      <div class="comment" style="font-size:20px">Comment “Summer”!</div>
    </div>
    <div class="handle">@PaulaWrenLive</div>
  </section>

</main>
</body>
</html>
```